Wordpress website design for children’s entertainment agency

What is the aim of the website?

The aim for the website is to attract potential bookers and to get them to respond to the Call to action: contact the entertainer - phone call/request a call back/completing a form.
All the information needs to be easy to access and navigate to, especially on mobile view.
The call to action needs to be clear and easy to navigate.

What I need:

Critical - This website needs to look good on all devices.
Easy navigation on a mobile device is essential so the elements need to be bold and easy to click on with a thumb (when in mobile view)

The ‘grid area’ needs to be graphics based with simple descriptions, i.e. ‘magic shows’, Circus Clowns, Face painting, Costume Characters, Party Host, Carnival Parties, Balloon Sculpting, DJ and MC, Princess Parties, Holiday Parties, Fun Add Ons and Contact.

See: http://www.jollyvornick.com/
and http://tinyrevelnest.com/
Updates

I would like to see a sample page layout as well to see how your design would be carried through the site layout in the inside pages.

Target Market(s)

The site visitors are mainly mums, aged between 25 - 41. Other visitors will included event organisers looking for entertainment services for baptism, communions and sweet 16’s

Industry/Entity Type

Entertainment Industry

Number of Pages Required

1 page

Font styles to use
Sans Serif

Colors
6c459b
fbed22
0493ce

Requirements
Must have
• Critical - This website needs to look good on all devices.
• Easy navigation on a mobile device is essential so the elements need to be bold and easy to click on with a thumb (when in mobile view)
• The ‘grid area’ needs to be graphics based with simple descriptions, i.e. ‘magic shows’, Circus Clowns, Face painting, Costume Characters, Party Host, Carnival Parties, Balloon Sculpting, DJ and MC, Princess Parties, Holiday Parties, Fun Add Ons and Contact.
• See: http://www.jollyvornick.com/
• and http://tinyrevelnest.com/
Nice to have
• clean looking and fun with an element of ‘Plumbo’ and stars (this is the exciting site http://gormansjoydome.com/index.html)

```html
<!DOCTYPE html>
<html lang="en">
<head>
<meta charset="utf-8">
<title>Gormans Joy Dome – Children's Entertainment</title>
<link href="https://fonts.googleapis.com/css2?family=Bubblegum+Sans&family=Open+Sans:wght@400;600&display=swap" rel="stylesheet">
<style>
:root{
  --purple:#6c459b;
  --purple-soft:#7450a3;
  --yellow:#fbed22;
  --blue:#0493ce;
  --white:#ffffff;
  --ink:#3a2a1a;
  --text:#444444;
  --black:#111111;
}
*{box-sizing:border-box;margin:0;padding:0}
html,body{width:1200px;height:2230px;overflow:hidden}
body{background:var(--purple);font-family:"Open Sans",sans-serif;color:var(--text);position:relative}

.brand{position:absolute;left:100px;top:95px;display:flex;align-items:center;gap:14px}
.brand-dot{width:58px;height:58px;border-radius:50%;background:var(--yellow)}
.brand-name{font-family:"Bubblegum Sans",cursive;font-size:36px;color:var(--yellow);line-height:1}

.phone{position:absolute;right:100px;top:92px;color:var(--white);font-family:"Bubblegum Sans",cursive;font-size:22px}
.header-cta{position:absolute;right:100px;top:137px;width:120px;height:38px;background:var(--yellow);color:var(--ink);font-family:"Bubblegum Sans",cursive;font-size:20px;display:flex;align-items:center;justify-content:center;border-radius:2px}

.main-nav{position:absolute;left:100px;top:232px;width:1000px;height:67px;display:flex;gap:2px}
.main-nav a{flex:1;background:var(--yellow);color:var(--ink);text-decoration:none;font-family:"Bubblegum Sans",cursive;font-size:16px;text-transform:uppercase;display:flex;align-items:center;justify-content:center}
.main-nav a.active{background:var(--blue);color:var(--white)}

.hero{position:absolute;left:100px;top:320px;width:1000px;height:333px;background:#000;overflow:hidden}
.hero-photo{position:absolute;left:294px;top:0;width:640px;height:333px;background:radial-gradient(ellipse at 65% 45%,#e8d8d0 0%,#3050b8 28%,#c83a2a 55%,#e0a020 75%,#000 100%)}
.hero-copy{position:absolute;left:42px;top:96px;font-family:"Bubblegum Sans",cursive;text-transform:uppercase}
.hero-copy .line1{color:var(--white);font-size:26px}
.hero-copy .line2{color:var(--yellow);font-size:42px;line-height:1.1}
.hero-dots{position:absolute;left:48px;top:190px;display:flex;gap:6px}
.hero-dots span{width:7px;height:7px;border-radius:50%;background:#aaa}
.hero-dots span:first-child{background:var(--yellow)}

.service-grid{position:absolute;left:100px;top:687px;width:710px;display:grid;grid-template-columns:repeat(4,171px);grid-template-rows:repeat(3,226px);column-gap:9px;row-gap:23px}
.service-tile{position:relative;overflow:hidden}
.service-tile .label{position:absolute;left:0;bottom:0;width:100%;height:46px;background:rgba(255,255,255,.72);border-top:3px solid var(--yellow);clip-path:polygon(0 0,82% 0,100% 100%,0 100%);font-family:"Bubblegum Sans",cursive;font-size:15px;color:var(--ink);padding:14px 0 0 13px}

.side-card{position:absolute;left:827px;width:273px;background:var(--yellow);border-radius:10px}
.contact-card{top:681px;height:538px;padding:18px 22px}
.side-card h2{font-family:"Bubblegum Sans",cursive;font-weight:400;color:var(--ink);font-size:31px;margin-bottom:16px}
.field{background:var(--white);border-radius:10px;height:45px;margin-bottom:16px;font-size:12px;color:#333;padding:14px 13px;box-shadow:2px 3px 4px rgba(0,0,0,.25)}
.field.message{height:124px}
.submit{display:inline-flex;width:96px;height:40px;border-radius:8px;background:var(--black);color:var(--white);font-family:"Bubblegum Sans",cursive;font-size:15px;align-items:center;justify-content:center;margin-top:10px}
.social-card{top:1237px;height:176px;padding:22px 28px}
.social-row{display:flex;gap:8px;margin-left:-10px}
.social-row span{width:55px;height:55px;border-radius:50%;background:var(--blue)}

.welcome{position:absolute;left:100px;top:1448px;width:1000px;height:272px;background:var(--white);border-radius:10px;padding:26px 48px;text-align:center}
.welcome h1{font-family:"Bubblegum Sans",cursive;font-weight:400;color:var(--purple);font-size:40px;text-transform:uppercase;margin-bottom:14px}
.welcome p{font-size:12px;line-height:1.75;color:var(--text);margin-bottom:18px}

.footer-col{position:absolute;top:1760px;color:var(--white)}
.footer-col h3{font-family:"Bubblegum Sans",cursive;font-weight:400;font-size:30px;margin-bottom:18px}
.location{left:100px}
.map{width:320px;height:137px;background:#d9d6cc;border-radius:2px}
.quick-links{left:537px}
.quick-links a{display:block;color:#eee;text-decoration:none;font-size:13px;line-height:21.5px}
.mailing{left:812px;width:288px}
.mailing p{font-size:12.5px;line-height:1.6;color:#ddd;margin-bottom:15px}
.mail-input{background:var(--white);height:47px;border-radius:2px;color:#222;font-size:12px;padding:16px}
.subscribe{display:inline-flex;margin-top:21px;width:120px;height:43px;background:var(--yellow);color:var(--ink);font-family:"Bubblegum Sans",cursive;font-size:20px;align-items:center;justify-content:center;border-radius:2px}
.copyright{position:absolute;left:100px;top:1996px;font-size:12px;color:#ddd}

.kids-band{position:absolute;left:205px;top:2052px;width:825px;height:178px;background:linear-gradient(180deg,rgba(236,196,150,.55),rgba(120,100,150,.4))}
</style>
</head>
<body>

<header>
  <div class="brand"><span class="brand-dot"></span><span class="brand-name">Gormans Joy Dome</span></div>
  <div class="phone">Phone No: 718–555–0142</div>
  <a class="header-cta">Contact Us</a>
</header>

<nav class="main-nav">
  <a class="active">Home</a><a>About</a><a>Areas Covered</a><a>Sevices</a><a>Testimonials</a><a>Contact</a><a>Fun Stuff</a>
</nav>

<section class="hero">
  <div class="hero-photo" role="img" aria-label="Photo of a clown in a striped costume tipping a top hat"></div>
  <div class="hero-copy"><div class="line1">Your Children's and Family's</div><div class="line2">Entertainment</div></div>
  <div class="hero-dots"><span></span><span></span><span></span></div>
</section>

<section class="service-grid">
  <div class="service-tile" role="img" aria-label="Photo of a magician performing on a street" style="background:linear-gradient(180deg,#8a8a8a,#5e5e5e)"><span class="label">Magicians</span></div>
  <div class="service-tile" role="img" aria-label="Photo of clowns in a park" style="background:linear-gradient(180deg,#7d9160,#9aa46e)"><span class="label">Clowns</span></div>
  <div class="service-tile" role="img" aria-label="Photo of party stage lights" style="background:linear-gradient(180deg,#1a5aa8,#16456e)"><span class="label">DJ/MC Services</span></div>
  <div class="service-tile" role="img" aria-label="Photo of painted octopus artwork on an arm" style="background:linear-gradient(180deg,#5a8a4a,#3a5a34)"><span class="label">Face Painting</span></div>
  <div class="service-tile" role="img" aria-label="Photo of a boy showing glitter art on his arm" style="background:linear-gradient(180deg,#9aacb8,#4a505e)"><span class="label">Glimmer Art</span></div>
  <div class="service-tile" role="img" aria-label="Photo of a carnival performer in a striped outfit" style="background:linear-gradient(180deg,#f0eeec,#dcd6d0)"><span class="label">Carnival Parties</span></div>
  <div class="service-tile" role="img" aria-label="Photo of a balloon sculpture bicycle" style="background:linear-gradient(180deg,#d6ecf6,#b8cfe8)"><span class="label">Balloon Sculpting</span></div>
  <div class="service-tile" role="img" aria-label="Photo of a party host with a parachute game" style="background:linear-gradient(180deg,#4a6a42,#9a9a6a)"><span class="label">Party Host</span></div>
  <div class="service-tile" role="img" aria-label="Photo of a costumed character at a popcorn stand" style="background:linear-gradient(180deg,#5a5aa0,#b85a5a)"><span class="label">Fun Foods</span></div>
  <div class="service-tile" role="img" aria-label="Photo of a child with a painted mask" style="background:linear-gradient(180deg,#3a2a2e,#8a4a4a)"><span class="label">Arts &amp; Crafts</span></div>
  <div class="service-tile" role="img" aria-label="Photo of a stilt walker in front of a ferris wheel" style="background:linear-gradient(180deg,#7aaee0,#a8c4dc)"><span class="label">Specialty Acts</span></div>
  <div class="service-tile" role="img" aria-label="Photo of a performer in a yellow princess gown" style="background:linear-gradient(180deg,#8a7a58,#d6bc5a)"><span class="label">Princess Parties</span></div>
</section>

<aside class="side-card contact-card">
  <h2>Contact Us</h2>
  <div class="field">Email</div>
  <div class="field">Name of Child</div>
  <div class="field">Phone Number</div>
  <div class="field">Postal Code</div>
  <div class="field message">Message</div>
  <span class="submit">Submit</span>
</aside>

<aside class="side-card social-card">
  <h2>Social media</h2>
  <div class="social-row" aria-label="Social media links"><span></span><span></span><span></span><span></span></div>
</aside>

<section class="welcome">
  <h1>Welcome to Gormans Joy Dome!</h1>
  <p>Have you ever heard the expression "make your own fun"? Well, when you call Gorman's Joy Dome, you don't have to! We make all the fun you'll need, and bring it straight to you. Clowns, Magicians, Face Painting, Balloon Animals, Jugglers, Party Princesses, Carnivals and much more, we create all of the fun that anyone could ever want!</p>
  <p>Our children's party entertainers appeal to your sense of fun regardless of age and we have a wide range of party services .Yes, We can come to your back yard party, catering hall, restaurant, Birthday party, communion, sweet sixteen's, christenings, baptism, bar mitzvah, bat mitzvah We service New York: Staten Island, NY, Brooklyn, NY, NYC and New Jersey, We guaranteed to make your party or special event a memorable one!</p>
</section>

<footer>
  <div class="footer-col location">
    <h3>Our Location</h3>
    <div class="map" role="img" aria-label="Street map showing the location"></div>
  </div>
  <div class="footer-col quick-links">
    <h3>Quick Links</h3>
    <a>Home</a><a>About</a><a>Areas Covered</a><a>Sevices</a><a>Testimonials</a><a>Contact</a><a>Fun stuff</a>
  </div>
  <div class="footer-col mailing">
    <h3>Join our mailing list</h3>
    <p>Subscribe newsletter to receive the latest news and updates direct to your inbox.</p>
    <div class="mail-input">Enter Your Mail Id</div>
    <span class="subscribe">Subscribe</span>
  </div>
  <div class="copyright">© 2015 gormansjoydome.com.&nbsp; All rights reserved.</div>
  <div class="kids-band" role="img" aria-label="Illustration of six cartoon children standing in a row"></div>
</footer>

</body>
</html>
```